Business Card Design for Kind Helper

I am starting my own consultancy business, using what I learned in marketing and advertising to help Non -profits with marketing and communications needs. I need a professional business card design to hand out to my clients.

My business name is “Outreach2Kindness” my vision is that this need this to be reflective of marketing doing good for the world through the power of communications. I like the color palettes in olives, creams and oranges but am open to design options.
In addition to the cards I am asking for separate file for the logo and will need a JPG, PSD Vector File.

Information to go on the card:

Morwenna Calloway
Marketing Consultant
Email: outreach2kindness@mailbrook.com, callowaym1@brinmoreu.edu
Website: Outreach2Kindness.com

Communications

```html
<!DOCTYPE html>
<html lang="en">
<head>
<meta charset="utf-8">
<title>Outreach2Kindness Business Card</title>
<link rel="stylesheet" href="https://fonts.googleapis.com/css2?family=Exo+2:wght@500&family=Arimo:wght@400&display=swap">
<style>
  :root {
    --card-blue: #1a69b3;
    --accent-light: #7a95cc;
    --paper: #ffffff;
    --bg-light: #8a8a8a;
    --bg-dark: #555555;
    --text-light: #ffffff;
  }
  * { margin: 0; padding: 0; box-sizing: border-box; }
  html, body { width: 1200px; height: 1000px; overflow: hidden; }
  body {
    position: relative;
    background: linear-gradient(135deg, var(--bg-light) 0%, #838383 55%, var(--bg-dark) 100%);
    font-family: "Arimo", Arial, sans-serif;
  }
  .card {
    position: absolute;
    box-shadow: 1px 2px 3px rgba(0,0,0,0.35);
    overflow: hidden;
  }
  .card-front {
    left: 37px; top: 50px; width: 543px; height: 316px;
    background: var(--card-blue);
    color: var(--text-light);
  }
  .card-front .corner-bands { position: absolute; inset: 0; }
  .person { position: absolute; left: 282px; top: 38px; }
  .person-name {
    font-family: "Exo 2", Arial, sans-serif;
    font-weight: 500;
    font-size: 25px;
    letter-spacing: 0.5px;
    line-height: 1;
  }
  .person-role { font-size: 14.5px; margin-top: 4px; }
  .contact-list {
    position: absolute; left: 52px; top: 214px;
    list-style: none; font-size: 15px;
  }
  .contact-list li { display: flex; align-items: center; height: 21px; }
  .contact-list svg { width: 13px; height: 13px; margin-right: 8px; flex: none; }
  .card-back {
    left: 614px; top: 47px; width: 544px; height: 319px;
    background: var(--paper);
    display: flex; align-items: center; justify-content: center; gap: 16px;
  }
  .brand-square {
    width: 34px; height: 34px;
    background: var(--card-blue);
  }
  .brand-name {
    font-family: "Arimo", Arial, sans-serif;
    font-weight: 400;
    font-size: 32px;
    color: var(--card-blue);
    letter-spacing: 0.5px;
  }
</style>
</head>
<body>
  <section class="card card-front">
    <svg class="corner-bands" width="543" height="316" viewBox="0 0 543 316" aria-hidden="true">
      <polygon points="0,0 70,0 0,70" fill="var(--accent-light)"/>
      <polygon points="84,0 96,0 0,96 0,84" fill="var(--accent-light)"/>
      <polygon points="543,196 543,316 423,316" fill="var(--accent-light)"/>
      <polygon points="543,172 543,184 411,316 399,316" fill="var(--accent-light)"/>
    </svg>
    <div class="person">
      <div class="person-name">Morwenna Calloway</div>
      <div class="person-role">Marketing Consultant</div>
    </div>
    <ul class="contact-list">
      <li>
        <svg viewBox="0 0 13 13"><rect x="3" y="0.5" width="7" height="12" rx="1" fill="#fff"/><rect x="4.3" y="2" width="4.4" height="4" fill="var(--card-blue)"/></svg>
        555.014.2870
      </li>
      <li>
        <svg viewBox="0 0 13 13"><rect x="0.5" y="3" width="12" height="8" fill="#fff"/><path d="M0.5 3 L6.5 7.5 L12.5 3" fill="none" stroke="var(--card-blue)" stroke-width="1"/></svg>
        outreach2kindness@mailbrook.com
      </li>
      <li>
        <svg viewBox="0 0 13 13"><g fill="none" stroke="#fff" stroke-width="1.1"><circle cx="6.5" cy="6.5" r="5.5"/><ellipse cx="6.5" cy="6.5" rx="2.3" ry="5.5"/><line x1="1" y1="6.5" x2="12" y2="6.5"/></g></svg>
        Outreach2Kindness.com
      </li>
    </ul>
  </section>

  <section class="card card-back">
    <span class="brand-square" aria-hidden="true"></span>
    <span class="brand-name">Outreach2Kindness</span>
  </section>
</body>
</html>
```